Scientific project description

Here is a project description related to cellular mechanics, showing above the forces acting on cells in the tissues of our body. The forces on single cells are there to depict how forces are acting on cells (pressure squeezes the cell, shear flow is pushing the upward parts of the cell, tension pulls one part of the cell, strain is stretching the whole cell; the single cell images are to be found also on the last page). Intense red/purple are used to indicate that the forces are stressful (the colors to be used do not need to be exactly like these colors). The picture in the middle is a view of cells (same picture on next page if that needs to be modified). At the left, a description of what happens when everything is going well, i.e. the body stays healthy. At the right, if you dysfunction you get disease. Green nuances were used to indicate health, brownish, perhaps not so pleasant nuances were used to indicate disease. Below are the steps of the project.

On the whole, we're rather happy with the concept description as such, but it should look a little bit nicer. To many color nuances give a "noisy" impression, fonts could be nicer, layout more crisp, and the text on the steps should be more readable. We would also like to have two versions of the same picture, one with black background, one with white.

Target Market(s)

Scientists that are evaluating our project

Requirements
Must have
• Easy to grasp the idea, easy to read and understand the underlying idea.
Nice to have
• Would be good to have the Concept title ("Pelvoran Concept and Envisioned Project Progression) on top of the figure as indicated in the second brief picture submitted.

```html
<!DOCTYPE html>
<html lang="en">
<head>
<meta charset="utf-8">
<title>Pelvoran – Concept and Envisioned Project Progression</title>
<link rel="stylesheet" href="https://fonts.googleapis.com/css2?family=Josefin+Sans:wght@400;600;700&family=Raleway:wght@400;500&display=swap">
<style>
  :root{
    --bg:#000;
    --white:#fff;
    --green:#4cb35a;
    --green-deep:#1c5a2a;
    --green-dark:#0f4a1e;
    --green-light:#8fd67f;
    --peach:#f2b084;
    --brown:#8a4a22;
    --brown-dark:#6e3512;
    --pressure-top:#e0703a;
    --pressure-bottom:#c8202e;
    --shear-top:#c8202e;
    --shear-bottom:#a8192a;
    --tension-top:#b0162c;
    --tension-bottom:#5e0a1c;
    --strain-top:#9a2a90;
    --strain-bottom:#6a2a8a;
    --label-pressure:#f2a23a;
    --label-shear:#c8202e;
    --label-tension:#c8202e;
    --label-strain:#8a3aa0;
    --hex-force:#d9582c;
    --hex-response:#c8202e;
    --hex-disease:#7a0f2a;
    --hex-machinery:#7e2a8e;
    --hex-targets:#8a5a38;
    --hex-prevention:#134a1f;
    --hex-therapies:#4cb35a;
  }
  *{box-sizing:border-box;margin:0;padding:0}
  html,body{width:1200px;height:1000px;overflow:hidden;background:var(--bg)}
  .canvas{position:relative;width:1200px;height:1000px;background:var(--bg);color:var(--white)}
  .project-title{position:absolute;top:100px;left:0;width:1200px;text-align:center;
    font-family:"Josefin Sans",sans-serif;font-weight:600;font-size:50px;letter-spacing:1px;line-height:1;color:var(--white)}
  .project-subtitle{position:absolute;top:156px;left:0;width:1200px;text-align:center;
    font-family:"Raleway",sans-serif;font-weight:400;font-size:26px;color:var(--white)}
  .force-card{position:absolute;width:137px}
  .force-card__tab{position:relative;height:34px;background:var(--white);border-radius:8px 8px 0 0;
    font-family:"Josefin Sans",sans-serif;font-weight:600;font-size:14px;letter-spacing:3px;
    text-align:center;line-height:36px}
  .force-card__tab::after{content:"";position:absolute;left:50%;bottom:-9px;margin-left:-9px;
    border-left:9px solid transparent;border-right:9px solid transparent;border-top:10px solid var(--white)}
  .force-card__body{height:106px;border-radius:0 0 8px 8px}
  .force-card--pressure{left:303px;top:257px}
  .force-card--pressure .force-card__tab{color:var(--label-pressure)}
  .force-card--pressure .force-card__body{background:linear-gradient(var(--pressure-top),var(--pressure-bottom))}
  .force-card--shear{left:456px;top:243px}
  .force-card--shear .force-card__tab{color:var(--label-shear)}
  .force-card--shear .force-card__body{background:linear-gradient(var(--shear-top),var(--shear-bottom))}
  .force-card--tension{left:608px;top:243px}
  .force-card--tension .force-card__tab{color:var(--label-tension)}
  .force-card--tension .force-card__body{background:linear-gradient(var(--tension-top),var(--tension-bottom))}
  .force-card--strain{left:760px;top:257px}
  .force-card--strain .force-card__tab{color:var(--label-strain)}
  .force-card--strain .force-card__body{background:linear-gradient(var(--strain-top),var(--strain-bottom))}
  .diagram{position:absolute;left:0;top:0}
  .label{font-family:"Raleway",sans-serif;font-size:13px}
  .hub-title{font-family:"Josefin Sans",sans-serif;font-weight:600;font-size:22px;letter-spacing:.5px}
  .step-label{font-family:"Josefin Sans",sans-serif;font-weight:600;font-size:11px;letter-spacing:.3px}
</style>
</head>
<body>
<main class="canvas">
  <h1 class="project-title">PELVORAN</h1>
  <p class="project-subtitle">Concept and Envisioned Project Progression</p>

  <section class="force-card force-card--pressure">
    <div class="force-card__tab">PRESSURE</div>
    <div class="force-card__body" role="img" aria-label="Cell outline squeezed flat by downward pressure arrows"></div>
  </section>
  <section class="force-card force-card--shear">
    <div class="force-card__tab">SHEAR</div>
    <div class="force-card__body" role="img" aria-label="Cell outline pushed sideways by shear flow arrows"></div>
  </section>
  <section class="force-card force-card--tension">
    <div class="force-card__tab">TENSION</div>
    <div class="force-card__body" role="img" aria-label="Cell outline pulled upward at one point by tension arrows"></div>
  </section>
  <section class="force-card force-card--strain">
    <div class="force-card__tab">STRAIN</div>
    <div class="force-card__body" role="img" aria-label="Cell outline stretched in both directions by strain arrows"></div>
  </section>

  <svg class="diagram" width="1200" height="1000" viewBox="0 0 1200 1000">
    <defs>
      <linearGradient id="micro" x1="0" y1="0" x2="1" y2="1">
        <stop offset="0" stop-color="#1f5a1c"/>
        <stop offset=".5" stop-color="#2e7a24"/>
        <stop offset="1" stop-color="#143d14"/>
      </linearGradient>
      <marker id="arrow" viewBox="0 0 10 10" refX="5" refY="5" markerWidth="5" markerHeight="5" orient="auto">
        <path d="M0 0 L10 5 L0 10 z" fill="#fff"/>
      </marker>
    </defs>

    <!-- connectors from force cards -->
    <g fill="none" stroke="#fff" stroke-width="2.5">
      <path d="M369 414 V428 H548 V460" marker-end="url(#arrow)"/>
      <path d="M522 400 V412 H580 V460" marker-end="url(#arrow)"/>
      <path d="M676 400 V412 H620 V460" marker-end="url(#arrow)"/>
      <path d="M828 414 V428 H648 V460" marker-end="url(#arrow)"/>
    </g>
    <g stroke="#fff" stroke-width="3" fill="url(#micro)" role="img" aria-label="Micrograph thumbnails of stained cells">
      <circle cx="369" cy="398" r="17"/>
      <circle cx="522" cy="383" r="17"/>
      <circle cx="676" cy="383" r="17"/>
      <circle cx="828" cy="398" r="17"/>
    </g>

    <!-- central hub -->
    <polygon points="485,580 540,487 660,487 715,580 660,675 540,675" fill="url(#micro)" stroke="#7fcf74" stroke-width="1.5" role="img" aria-label="Fluorescence micrograph of cells with green cytoskeleton and red stained contacts"/>
    <text class="hub-title" x="600" y="588" text-anchor="middle" fill="#fff">MECHANOSTASIS</text>

    <!-- left: health side -->
    <polygon points="383,497 512,497 498,523 383,523" fill="var(--green)"/>
    <polygon points="484,523 498,497 520,497 506,523" fill="var(--green-deep)"/>
    <text class="label" x="398" y="515" fill="#fff">Cell fitness</text>

    <polygon points="288,562 478,562 464,602 288,602" fill="var(--green-dark)" stroke="#2d7a3a" stroke-width="1"/>
    <text class="label" x="373" y="579" text-anchor="middle" fill="#fff">Functional cellular</text>
    <text class="label" x="373" y="594" text-anchor="middle" fill="#fff">machineries</text>
    <polygon points="483,565 470,582 483,599 490,599 477,582 490,565" fill="#fff"/>

    <path d="M376 602 V652 H394" fill="none" stroke="#fff" stroke-width="2" marker-end="url(#arrow)"/>
    <polygon points="402,640 512,640 498,666 402,666" fill="var(--green)"/>
    <polygon points="484,666 498,640 520,640 506,666" fill="var(--green-deep)"/>
    <text class="label" x="422" y="658" fill="#fff">Health</text>

    <!-- right: disease side -->
    <polygon points="677,523 691,497 823,497 823,523" fill="var(--peach)"/>
    <polygon points="677,523 691,497 713,497 699,523" fill="var(--brown)"/>
    <text class="label" x="738" y="515" fill="#3a1a08">Cell Frailty</text>

    <polygon points="728,562 912,562 912,602 742,602" fill="var(--brown)" stroke="#a0623a" stroke-width="1"/>
    <text class="label" x="823" y="579" text-anchor="middle" fill="#fff">Disfunctional cellular</text>
    <text class="label" x="823" y="594" text-anchor="middle" fill="#fff">machineries</text>
    <polygon points="717,565 730,582 717,599 710,599 723,582 710,565" fill="#fff"/>

    <path d="M824 602 V652 H806" fill="none" stroke="#fff" stroke-width="2" marker-end="url(#arrow)"/>
    <polygon points="677,666 691,640 795,640 795,666" fill="var(--peach)"/>
    <polygon points="677,666 691,640 713,640 699,666" fill="var(--brown)"/>
    <text class="label" x="733" y="658" fill="#3a1a08">Disease</text>

    <!-- project steps -->
    <g fill="none" stroke-width="7">
      <polygon points="292,763 320,714 378,714 406,763 378,812 320,812" stroke="var(--hex-force)"/>
      <polygon points="377,812 405,763 463,763 491,812 463,861 405,861" stroke="var(--hex-response)"/>
      <polygon points="462,763 490,714 548,714 576,763 548,812 490,812" stroke="var(--hex-disease)"/>
      <polygon points="547,812 575,763 633,763 661,812 633,861 575,861" stroke="var(--hex-machinery)"/>
      <polygon points="633,763 661,714 719,714 747,763 719,812 661,812" stroke="var(--hex-targets)"/>
      <polygon points="718,812 746,763 804,763 832,812 804,861 746,861" stroke="var(--hex-prevention)"/>
      <polygon points="803,763 831,714 889,714 917,763 889,812 831,812" stroke="var(--hex-therapies)"/>
    </g>
    <g class="step-label" fill="#fff" text-anchor="middle">
      <text x="349" y="759">MECHANICAL</text><text x="349" y="772">FORCE MODELS</text>
      <text x="436" y="800">CELL, TISSUE</text><text x="436" y="813">AND ORGAN</text><text x="436" y="826">RESPONSES</text>
      <text x="519" y="759">DISEASE</text><text x="519" y="772">MODELS</text>
      <text x="604" y="805">CELLULAR</text><text x="604" y="818">MACHINERIES</text>
      <text x="690" y="761">CRITICAL</text><text x="690" y="774">TARGETS</text>
      <text x="775" y="815">PREVENTION</text>
      <text x="860" y="767">THERAPIES</text>
    </g>
  </svg>
</main>
</body>
</html>
```